Business Card Design

I am an insurance agent and do most of my work from home. I want to change the attached business card to reflect my home address, cell phone number and email address. Perhaps I want my business address and business phone and fax on the back. I like the card attached. But it has all houses. I would like a house, car, motorcycle, boat, business and life insurance logos instead of just houses. My work address is KMT Insurance Agency; 5816 Wexley Parkway, Suite 410; Falls Church, Virginia 22046-3917. My home address is 931 Millbrook Lane; Woodbridge, Virginia 22193-2684. I want it to have my name and the company name and my address. I like everything spelled out. I do not like abbreviations. I want a card that stands out. Maybe even a little bit silly like the one attached but still to be professional.
Updates

I want my home address on the front and work address on the back.

Home: 931 Millbrook Lane; Woodbridge, Virginia 22193-2684

Work: 5816 Wexley Parkway, Suite 410; Falls Church, Virginia 22046-3917
                                                                

I re-read what I wrote and tried to make it clearer; so there are some minor changes.

The PDF business card I uploaded did not appear to be readable.  I scanned it in as a JPG and uploaded it.  It is not as clear but is readable.  I just want you to see what I currently have and sort of like.

Target Market(s)

Insurance Customers. Mostly by mail or email

Industry/Entity Type

Life Insurance

Contact Information for Business Card

KMT Insurance Agency Dennis R Whitcombe
931 Millbrook Lane; Woodbridge, Virginia 22193-2684
Cell phone: (703) 555-4162 DWHITCOMBE@MAILNEST.EXAMPLE

Colors

Designer to choose colors to be used in the design.

Requirements
Must have
• On the front I want my home information and on the back perhaps my office information. I go to the office once a week or less. So I want to be contacted by email or my cell. I want them to mail stuff to my house. I don't want them to contact my office unless they cannot reach me. I have my email address in all capitals because it starts with an "L" and that could be a 1, I, or L. I have another email address: whitcombe@postvale.example and perhaps I should use that one or both.
Nice to have
• Auto, Boat, Business, Commercial, Home, Life & Health, Motorcycle.
It would be nice to say this across the card if not too long and to have some of these logos displayed, per the attached card.
Should not have
• I like things spelled out, such as Street rather than ST or Virginia rather than VA. But Cell Phone or Cell as you think best.

```html
<!DOCTYPE html>
<html lang="en">
<head>
<meta charset="utf-8">
<title>KMT Insurance Agency – Business Card</title>
<link href="https://fonts.googleapis.com/css2?family=Open+Sans:wdth,wght@75..100,400;75..100,600;75..100,700&display=swap" rel="stylesheet">
<style>
  :root {
    --brand-blue: #2b5aa0;
    --brand-blue-dark: #234c8a;
    --accent-orange: #e8731e;
    --ink: #2f2f2f;
    --paper: #ffffff;
    --backdrop: #e9e9e7;
    --photo-light: #d8d2cc;
    --photo-dark: #3a3f4a;
  }
  * { box-sizing: border-box; margin: 0; padding: 0; }
  html, body { width: 1200px; height: 1023px; overflow: hidden; }
  body {
    background: var(--backdrop);
    font-family: "Open Sans", Arial, sans-serif;
    position: relative;
  }
  .card {
    position: absolute;
    width: 660px;
    height: 378px;
    border-radius: 3px;
    box-shadow: 0 10px 28px rgba(0,0,0,.18);
    overflow: hidden;
  }
  .icon-row { display: flex; gap: 8px; }
  .icon-badge { display: block; }

  /* Back of card */
  .card-back {
    left: 90px; top: 70px;
    background: var(--brand-blue);
    color: var(--paper);
    text-align: center;
  }
  .card-back .agency-name {
    font-stretch: 82%;
    font-weight: 700;
    font-size: 50px;
    line-height: 1;
    margin-top: 62px;
  }
  .card-back .service-list {
    font-stretch: 85%;
    font-size: 16px;
    margin-top: 12px;
  }
  .card-back .icon-row { justify-content: center; margin-top: 18px; gap: 10px; }
  .card-back .office-heading {
    font-stretch: 85%;
    font-weight: 700;
    font-size: 15px;
    margin-top: 44px;
  }
  .card-back .office-phones {
    display: flex; justify-content: center; gap: 18px;
    font-stretch: 85%; font-size: 15px; margin-top: 4px;
  }
  .card-back .office-address {
    font-stretch: 85%; font-size: 15px; margin-top: 4px;
  }
  .contact-line { display: inline-flex; align-items: center; gap: 6px; }
  .contact-icon { width: 15px; height: 15px; flex: none; }

  /* Front of card */
  .card-front {
    left: 450px; top: 520px;
    background: var(--paper);
    color: var(--ink);
  }
  .card-front .agency-name {
    position: absolute; left: 30px; top: 66px;
    color: var(--brand-blue);
    font-stretch: 82%;
    font-weight: 700;
    font-size: 38px;
    line-height: 1;
  }
  .card-front .service-list {
    position: absolute; left: 30px; top: 114px; width: 330px;
    font-stretch: 88%;
    font-size: 17px;
    line-height: 1.4;
  }
  .agent-block { position: absolute; left: 38px; top: 210px; }
  .agent-name {
    color: var(--accent-orange);
    font-stretch: 88%;
    font-weight: 600;
    font-size: 24px;
    line-height: 1.1;
  }
  .agent-title { font-stretch: 88%; font-size: 16px; margin-top: 2px; }
  .agent-contacts { margin-top: 12px; font-stretch: 88%; font-size: 14.5px; line-height: 1.6; }
  .agent-contacts .contact-line { display: flex; }
  .agent-photo {
    position: absolute; right: 0; top: 18px;
    width: 300px; height: 300px;
    background: radial-gradient(ellipse at 60% 35%, var(--photo-light) 0 32%, var(--photo-dark) 70%, var(--paper) 71%);
  }
  .address-band {
    position: absolute; left: 0; right: 0; bottom: 0; height: 60px;
    background: var(--brand-blue);
    color: var(--paper);
    display: flex; align-items: center; justify-content: space-between;
    padding: 0 14px 0 32px;
  }
  .home-address { font-stretch: 88%; font-size: 14.5px; line-height: 1.3; }
  .address-band .icon-row { gap: 4px; }
</style>
</head>
<body>
<svg width="0" height="0" style="position:absolute" aria-hidden="true">
  <defs>
    <symbol id="icon-car" viewBox="0 0 40 40">
      <path d="M9 23 L12 16 Q13 14 15 14 H25 Q27 14 28 16 L31 23 Q33 23 33 25 V29 H7 V25 Q7 23 9 23 Z M13 22 H27 L25 17 H15 Z" fill="currentColor" fill-rule="evenodd"/>
      <circle cx="12" cy="29" r="3" fill="currentColor"/><circle cx="28" cy="29" r="3" fill="currentColor"/>
    </symbol>
    <symbol id="icon-boat" viewBox="0 0 40 40">
      <path d="M20 8 V26 H10 Z" fill="currentColor"/><path d="M22 11 L29 26 H22 Z" fill="currentColor"/>
      <path d="M9 28 H31 L28 32 H12 Z" fill="currentColor"/>
      <path d="M8 34 Q12 32 16 34 T24 34 T32 34" stroke="currentColor" stroke-width="1.5" fill="none"/>
    </symbol>
    <symbol id="icon-briefcase" viewBox="0 0 40 40">
      <path d="M16 13 V11 H24 V13" stroke="currentColor" stroke-width="2" fill="none"/>
      <rect x="9" y="13" width="22" height="16" rx="2" fill="currentColor"/>
      <rect x="9" y="19" width="22" height="1.5" fill="var(--brand-blue)"/>
      <rect x="18" y="18" width="4" height="4" fill="var(--brand-blue)"/>
    </symbol>
    <symbol id="icon-building" viewBox="0 0 40 40">
      <rect x="12" y="8" width="16" height="24" fill="none" stroke="currentColor" stroke-width="2"/>
      <g fill="currentColor">
        <rect x="15" y="11" width="3" height="3"/><rect x="22" y="11" width="3" height="3"/>
        <rect x="15" y="16" width="3" height="3"/><rect x="22" y="16" width="3" height="3"/>
        <rect x="15" y="21" width="3" height="3"/><rect x="22" y="21" width="3" height="3"/>
        <rect x="18" y="26" width="4" height="6"/>
      </g>
    </symbol>
    <symbol id="icon-house" viewBox="0 0 40 40">
      <path d="M7 20 L20 9 L33 20 H29 V31 H11 V20 Z" fill="currentColor"/>
      <rect x="17" y="23" width="6" height="8" fill="var(--brand-blue)"/>
    </symbol>
    <symbol id="icon-life" viewBox="0 0 40 40">
      <path d="M20 31 L10 21 Q6 16 10 12 Q15 8 20 14 Q25 8 30 12 Q34 16 30 21 Z" fill="currentColor"/>
      <path d="M18 16 H22 V19 H25 V23 H22 V26 H18 V23 H15 V19 H18 Z" fill="var(--brand-blue)"/>
    </symbol>
    <symbol id="icon-motorcycle" viewBox="0 0 40 40">
      <circle cx="11" cy="27" r="5" fill="none" stroke="currentColor" stroke-width="2"/>
      <circle cx="29" cy="27" r="5" fill="none" stroke="currentColor" stroke-width="2"/>
      <path d="M11 27 L17 19 H24 L29 27 M22 19 L25 13 H28" stroke="currentColor" stroke-width="2.2" fill="none"/>
      <path d="M15 20 H25 L23 24 H17 Z" fill="currentColor"/>
    </symbol>
    <symbol id="badge-ring" viewBox="0 0 40 40">
      <circle cx="20" cy="20" r="18.5" fill="none" stroke="currentColor" stroke-width="2"/>
    </symbol>
    <symbol id="glyph-phone" viewBox="0 0 16 16">
      <circle cx="8" cy="8" r="8" fill="var(--accent-orange)"/>
      <path d="M4 6.5 Q8 4 12 6.5 L11 8 Q8 7 5 8 Z M5.5 9 H10.5 V11.5 H5.5 Z" fill="#fff"/>
    </symbol>
    <symbol id="glyph-mail" viewBox="0 0 16 16">
      <circle cx="8" cy="8" r="8" fill="var(--accent-orange)"/>
      <rect x="4" y="5.2" width="8" height="5.6" fill="#fff"/>
      <path d="M4 5.2 L8 8.4 L12 5.2" stroke="var(--accent-orange)" stroke-width="1" fill="none"/>
    </symbol>
  </defs>
</svg>

<section class="card card-back" aria-label="Back of card">
  <h1 class="agency-name">KMT Insurance Agency</h1>
  <p class="service-list">Auto, Boat, Business, Commercial, Home, Life &amp; Health, Motorcycle</p>
  <div class="icon-row" style="color:#fff">
    <svg class="icon-badge" width="54" height="54" aria-label="Auto"><use href="#badge-ring"/><use href="#icon-car"/></svg>
    <svg class="icon-badge" width="54" height="54" aria-label="Boat"><use href="#badge-ring"/><use href="#icon-boat"/></svg>
    <svg class="icon-badge" width="54" height="54" aria-label="Business"><use href="#badge-ring"/><use href="#icon-briefcase"/></svg>
    <svg class="icon-badge" width="54" height="54" aria-label="Commercial"><use href="#badge-ring"/><use href="#icon-building"/></svg>
    <svg class="icon-badge" width="54" height="54" aria-label="Home"><use href="#badge-ring"/><use href="#icon-house"/></svg>
    <svg class="icon-badge" width="54" height="54" aria-label="Life and Health"><use href="#badge-ring"/><use href="#icon-life"/></svg>
    <svg class="icon-badge" width="54" height="54" aria-label="Motorcycle"><use href="#badge-ring"/><use href="#icon-motorcycle"/></svg>
  </div>
  <p class="office-heading">Office Contact Details:</p>
  <div class="office-phones">
    <span class="contact-line"><svg class="contact-icon"><use href="#glyph-phone"/></svg>(703) 555-0931</span>
    <span class="contact-line"><svg class="contact-icon"><use href="#glyph-phone"/></svg>(703) 555-0932</span>
  </div>
  <p class="office-address">5816 Wexley Parkway, Suite 410, Falls Church, Virginia 22046-3917</p>
</section>

<section class="card card-front" aria-label="Front of card">
  <h2 class="agency-name">KMT Insurance Agency</h2>
  <p class="service-list">Auto, Boat, Business, Commercial, Home, Life &amp; Health, Motorcycle</p>
  <div class="agent-block">
    <p class="agent-name">Dennis R Whitcombe</p>
    <p class="agent-title">Insurance Agent</p>
    <div class="agent-contacts">
      <span class="contact-line"><svg class="contact-icon"><use href="#glyph-phone"/></svg>(703) 555-4162</span>
      <span class="contact-line"><svg class="contact-icon"><use href="#glyph-mail"/></svg>DWhitcombe@mailnest.example</span>
    </div>
  </div>
  <div class="agent-photo" role="img" aria-label="Portrait photograph of the insurance agent"></div>
  <div class="address-band">
    <p class="home-address">931 Millbrook Lane,<br>Woodbridge, Virginia 22193-2684</p>
    <div class="icon-row" style="color:#fff">
      <svg class="icon-badge" width="42" height="42" viewBox="0 0 40 40" aria-label="Auto"><use href="#badge-ring"/><use href="#icon-car"/></svg>
      <svg class="icon-badge" width="42" height="42" viewBox="0 0 40 40" aria-label="Boat"><use href="#badge-ring"/><use href="#icon-boat"/></svg>
      <svg class="icon-badge" width="42" height="42" viewBox="0 0 40 40" aria-label="Business"><use href="#badge-ring"/><use href="#icon-briefcase"/></svg>
      <svg class="icon-badge" width="42" height="42" viewBox="0 0 40 40" aria-label="Commercial"><use href="#badge-ring"/><use href="#icon-building"/></svg>
      <svg class="icon-badge" width="42" height="42" viewBox="0 0 40 40" aria-label="Home"><use href="#badge-ring"/><use href="#icon-house"/></svg>
      <svg class="icon-badge" width="42" height="42" viewBox="0 0 40 40" aria-label="Life and Health"><use href="#badge-ring"/><use href="#icon-life"/></svg>
      <svg class="icon-badge" width="42" height="42" viewBox="0 0 40 40" aria-label="Motorcycle"><use href="#badge-ring"/><use href="#icon-motorcycle"/></svg>
    </div>
  </div>
</section>
</body>
</html>
```